Business cards

We need business cards for the logo that you designed for our company. Something simple and clean.

Target Market(s)

Homeowners/ people looking for construction work

Industry/Entity Type

Construction

Contact Information for Business Card

Name: Doug Whitby, Number: 602-555-0174, Email: WhitbyBuildingCompany@mailbox-example.net ROC# 482063

Font styles to use
Serif

Colors

Designer to choose colors to be used in the design.

Requirements
Must have
• On one side of the card I would like to be all of the personal information I have put above along with the company logo that I have attached.
• On the other side of the card I would like the top half of the card to be the logo and then on the bottom half I would like to have the areas of construction we focus on along with an icon that represents it like the picture I have attached.
• Areas we focus on:
• Roofing, Kitchen and bath Remodel, Water Damage, Storm Damage, Fire Damage, Insurance Specialist
• If we could arrange those in alphabetical order.
Nice to have
• I have added 2 company logos a colorful one and a black one it would be nice to see a couple different options the black logo to be more simple and sleek and the colorful logo to be more colorful

```html
<!DOCTYPE html>
<html lang="en">
<head>
<meta charset="utf-8">
<title>Whitby Building Company – Business Cards</title>
<link href="https://fonts.googleapis.com/css2?family=Roboto:wght@400;500&family=Roboto+Condensed:wght@700&family=Open+Sans:wght@600&display=swap" rel="stylesheet">
<style>
  :root {
    --backdrop: #676767;
    --card-white: #ffffff;
    --brand-blue: #35a6d6;
    --brand-red: #e5262b;
    --ink: #2a2a2a;
    --rule: #c9c9c9;
    --tile: #ffffff;
  }
  * { margin: 0; padding: 0; box-sizing: border-box; }
  html, body { width: 1200px; height: 802px; overflow: hidden; }
  body { background: var(--backdrop); position: relative; font-family: "Roboto", sans-serif; }

  .card { position: absolute; top: 268px; width: 443px; height: 265px; }
  .card--front { left: 136px; background: var(--card-white); }
  .card--back { left: 624px; background: var(--brand-blue); }

  .wordmark {
    position: absolute; display: flex; align-items: center; gap: 8px;
    font-family: "Roboto Condensed", sans-serif; font-weight: 700;
    font-size: 23px; letter-spacing: 0.5px; text-transform: uppercase; line-height: 1;
  }
  .wordmark__square { width: 30px; height: 30px; flex: none; }
  .card--front .wordmark { right: 26px; top: 78px; color: var(--brand-blue); }
  .card--front .wordmark__square { background: var(--brand-red); }
  .card--back .wordmark { left: 50%; transform: translateX(-50%); top: 80px; color: var(--card-white); white-space: nowrap; }
  .card--back .wordmark__square { border: 3px solid var(--card-white); }

  .holder-name {
    position: absolute; left: 24px; top: 157px;
    font-family: "Roboto Condensed", sans-serif; font-weight: 700; font-size: 17px;
    color: var(--brand-blue);
  }
  .holder-name__last { color: var(--brand-red); }
  .divider { position: absolute; left: 24px; right: 26px; top: 188px; height: 1px; background: var(--rule); }

  .contact { position: absolute; left: 24px; top: 205px; font-size: 12.5px; color: var(--ink); line-height: 16px; list-style: none; }
  .contact li { display: flex; align-items: center; gap: 4px; }
  .contact svg { width: 10px; height: 10px; fill: var(--brand-blue); }
  .licence { position: absolute; right: 26px; top: 221px; font-size: 12.5px; color: var(--ink); line-height: 16px; }

  .services { position: absolute; left: 0; top: 155px; width: 100%; list-style: none; }
  .service { position: absolute; top: 0; width: 90px; margin-left: -45px; text-align: center; }
  .service__tile {
    width: 47px; height: 47px; margin: 0 auto; background: var(--tile); border-radius: 4px;
    display: flex; align-items: center; justify-content: center;
  }
  .service__tile svg { width: 32px; height: 32px; }
  .service__label {
    margin-top: 7px; font-family: "Open Sans", sans-serif; font-weight: 600;
    font-size: 10px; line-height: 12.5px; color: var(--card-white); text-transform: uppercase;
  }
</style>
</head>
<body>

<section class="card card--front">
  <div class="wordmark"><span class="wordmark__square"></span>Whitby Building Company</div>
  <h1 class="holder-name">DOUG <span class="holder-name__last">WHITBY</span></h1>
  <div class="divider"></div>
  <ul class="contact">
    <li><svg viewBox="0 0 24 24"><path d="M6.6 10.8a15 15 0 0 0 6.6 6.6l2.2-2.2c.3-.3.7-.4 1-.2 1.1.4 2.3.6 3.6.6.6 0 1 .4 1 1V20c0 .6-.4 1-1 1A17 17 0 0 1 3 4c0-.6.4-1 1-1h3.5c.6 0 1 .4 1 1 0 1.3.2 2.5.6 3.6.1.3 0 .7-.2 1z"/></svg>602-555-0174</li>
    <li><svg viewBox="0 0 24 24"><path d="M2 5h20v14H2z M2 5l10 8 10-8" stroke="#fff" stroke-width="1.5"/></svg>WhitbyBuildingCompany@mailbox-example.net</li>
  </ul>
  <p class="licence">ROC# 482063</p>
</section>

<section class="card card--back">
  <div class="wordmark"><span class="wordmark__square"></span>Whitby Building Company</div>
  <ul class="services">
    <li class="service" style="left:48px">
      <div class="service__tile"><svg viewBox="0 0 24 24"><path fill="#e5262b" d="M12 2c1 4 6 6 6 12a6 6 0 0 1-12 0c0-3 2-5 3-6 0 2 1 3 2 3-1-3 0-6 1-9z"/></svg></div>
      <p class="service__label">Fire<br>Damage</p>
    </li>
    <li class="service" style="left:111px">
      <div class="service__tile"><svg viewBox="0 0 24 24" fill="none" stroke="#35a6d6" stroke-width="2"><path d="M5 11l7-6 7 6M7 10v6h10v-6"/><path d="M2 14c1 4 4 7 10 7s9-3 10-7"/></svg></div>
      <p class="service__label">Insurance<br>Specialist</p>
    </li>
    <li class="service" style="left:192px">
      <div class="service__tile"><svg viewBox="0 0 24 24"><path fill="#e5262b" d="M2 12h20v2a5 5 0 0 1-5 5H7a5 5 0 0 1-5-5z M6 19l-1 2h2l1-2z M16 19l1 2h2l-1-2z"/><path d="M5 12V5a2 2 0 0 1 4 0" fill="none" stroke="#e5262b" stroke-width="1.5"/></svg></div>
      <p class="service__label">Kitchen &amp;<br>Bath Remodel</p>
    </li>
    <li class="service" style="left:266px">
      <div class="service__tile"><svg viewBox="0 0 24 24"><path fill="#35a6d6" d="M2 18l6-10h12l3 10z"/><path d="M7 18l5-10M12 18l5-10" stroke="#fff" stroke-width="1.5"/></svg></div>
      <p class="service__label">Roofing</p>
    </li>
    <li class="service" style="left:327px">
      <div class="service__tile"><svg viewBox="0 0 24 24" fill="none" stroke="#e5262b" stroke-width="1.8"><path d="M7 16H6a4 4 0 0 1 0-8 6 6 0 0 1 11-1 4.5 4.5 0 0 1 1 9h-1"/><path d="M13 12l-3 5h4l-3 5"/></svg></div>
      <p class="service__label">Storm<br>Damage</p>
    </li>
    <li class="service" style="left:392px">
      <div class="service__tile"><svg viewBox="0 0 24 24" fill="#35a6d6"><path d="M12 4c2 4 5 7 5 10a5 5 0 0 1-10 0c0-3 3-6 5-10z"/><circle cx="4" cy="15" r="1.6"/><circle cx="20" cy="14" r="1.6"/></svg></div>
      <p class="service__label">Water<br>Damage</p>
    </li>
  </ul>
</section>

</body>
</html>
```